Vorn Apparel Brochure Project

Looking for a brochure to send out with samples of our apparel. The name of our company is Vorn Apparel and we are distributors for 7.42. I have attached an older 7.42 brochure. I would like the brochure to be regular paper size with no folds.

Target Market(s)

Buyers working for large U.S. retail stores

Colors

Designer to choose colors to be used in the design.

Requirements
Must have
• Must look sleek and professional.

```html
<!DOCTYPE html>
<html lang="en">
<head>
<meta charset="utf-8">
<title>Vorn Apparel — Khadi Collection</title>
<link href="https://fonts.googleapis.com/css2?family=Noto+Serif:wght@300;400&family=Montserrat:wght@400&display=swap" rel="stylesheet">
<style>
  :root {
    --paper: #ffffff;
    --ink: #2b2b2b;
    --accent: #9b1c1c;
    --accent-text: #ffffff;
    --photo-dark: #3d4230;
    --photo-mid: #8c7a55;
    --photo-light: #d8c197;
    --dress-tone: #c9a57a;
  }
  html, body {
    margin: 0;
    padding: 0;
    overflow: hidden;
    background: var(--paper);
  }
  .page {
    position: relative;
    width: 848px;
    height: 1200px;
    background: var(--paper);
    overflow: hidden;
  }
  .intro {
    position: absolute;
    left: 53px;
    top: 352px;
    width: 310px;
    margin: 0;
    font-family: "Noto Serif", Georgia, serif;
    font-weight: 300;
    font-size: 25px;
    line-height: 49px;
    color: var(--ink);
    white-space: nowrap;
  }
  .intro .lead-word {
    font-size: 56px;
    line-height: 0;
    font-weight: 400;
    margin-right: 6px;
  }
  .feature-photo {
    position: absolute;
    left: 382px;
    top: 43px;
    width: 375px;
    height: 986px;
    background:
      linear-gradient(90deg, rgba(0,0,0,0) 0%, rgba(0,0,0,0) 40%, var(--dress-tone) 55%, #b98e64 100%),
      linear-gradient(180deg, var(--photo-dark) 0%, #5b6040 30%, var(--photo-mid) 60%, var(--photo-light) 100%);
  }
  .page-number {
    position: absolute;
    left: 755px;
    top: 1115px;
    width: 93px;
    height: 55px;
    background: var(--accent);
    color: var(--accent-text);
    font-family: "Montserrat", Arial, sans-serif;
    font-size: 34px;
    line-height: 55px;
    text-align: center;
    padding-right: 14px;
    box-sizing: border-box;
  }
</style>
</head>
<body>
  <main class="page">
    <p class="intro"><span class="lead-word">We</span> proudly present<br>
      the finest artisanal<br>
      luxury, hand-spun and<br>
      hand-woven (known as<br>
      “khadi) fabric products,<br>
      emphasizing the link<br>
      between farmers,<br>
      weavers, vegetable<br>
      dyers and block<br>
      printing traditions. This<br>
      result is a coherent and<br>
      meaningful fashion<br>
      garment line that<br>
      creates grounds for<br>
      ethical products.</p>

    <div class="feature-photo" role="img" aria-label="Model in a garden wearing a long strappy block-printed khadi dress with a small multicoloured check pattern"></div>

    <div class="page-number">2</div>
  </main>
</body>
</html>
```